NCCS Brochure Design

Northbrook Council of Clinical Standards (NCCS) needs a whole new brochure. I've upload EPS logos and past brochures. Our tagline is to "modernize healthcare" and we think our brochure should reflect that, so that's the purpose of this project.

NCCS is a proven leader in healthcare education, training and
consulting services for health professionals. We’ve earned a reputation for excellence in healthcare quality improvement and management.

NCCS works to improve healthcare quality by educating healthcare professionals about healthcare best practices. We focus on instructing our clients on how to plan for, measure, and improve healthcare quality in all facilities and facets such as:

Patient Safety
Infection Control
Performance Improvement
Risk Management
Compliance and Accreditation
Health and Hospital Administration
Health Insurance
Healthcare Financial Management
Facility Management and Safety

DESIGN SUGGESTIONS:

Brochure Size: 8.5 X 11 full size brochure or 8.5 X 11 trifold brochure

Number of Pages: 2 to 3

Colors: Feel free to use a wide array of colors but try to stay away from colors that are too loud, ex: Pink, Purple, Neon Green.

Themes: Professional, Educational

Designs:

Korvel by Tobias Lindqvar

Palvex Leaflet by Derek Ostland

Gears for assembly by Quintoru

Figura de Sr KT by vrpq

http://www.plimsark.com/post/48210736651/10-creative-brochure-designs

Don't limit yourself to these examples. However, these are examples we liked
Updates

Project Deadline Extended
Reason: We would like to see more designs

We want more full page designs than tri-fold 

We are considering both tri-fold and full-page but would like to see more full page designs 

Project Deadline Extended

Project Deadline Extended
Reason: Our lead designer making the decisions on this project has been fired. I apologize for the inconvenience. We want extend the project one last time

Project Deadline Extended

Target Market(s)

Students, Doctors, and Educational Professionals

Industry/Entity Type

Healthcare

Logo Text

asdfasdf

Font styles to use
Serif
Sans Serif
Decorative
Script

Requirements
Should not have
• Pink, Purple, Neon Green colors

```html
<!DOCTYPE html>
<html lang="en">
<head>
<meta charset="utf-8">
<title>NCCS Brochure</title>
<link rel="stylesheet" href="https://fonts.googleapis.com/css2?family=Oswald:wght@500;600&family=Open+Sans:wght@400;700&display=swap">
<style>
  :root {
    --band-blue: #1f7fce;
    --band-blue-light: #2a8fdc;
    --band-navy: #124a86;
    --heading-red: #b22a2a;
    --body-text: #3a3a3a;
    --logo-navy: #1c3f7a;
    --page-top: #ffffff;
    --page-bottom: #e9e9e9;
    --ring-white: #ffffff;
  }
  * { margin: 0; padding: 0; box-sizing: border-box; }
  html, body { width: 1200px; height: 925px; overflow: hidden; }
  body { background: #ffffff; }

  .brochure-page {
    position: relative;
    width: 1200px;
    height: 925px;
    overflow: hidden;
    background: linear-gradient(to bottom, var(--page-top) 55%, var(--page-bottom) 100%);
    font-family: "Open Sans", Arial, sans-serif;
  }

  .hero-band {
    position: absolute;
    left: 0; top: 0;
    width: 1200px; height: 266px;
    background: linear-gradient(to right, var(--band-blue) 0%, var(--band-blue-light) 100%);
  }
  .hero-rule {
    position: absolute;
    left: 0; top: 266px;
    width: 1200px; height: 17px;
    background: var(--band-navy);
  }
  .hero-title {
    position: absolute;
    left: 36px; top: 70px;
    width: 380px;
    font-family: "Oswald", "Arial Narrow", sans-serif;
    font-weight: 600;
    font-size: 36px;
    line-height: 43px;
    color: #ffffff;
    text-transform: uppercase;
    letter-spacing: 0.3px;
  }

  .hero-photo {
    position: absolute;
    top: 53px;
    width: 186px; height: 186px;
    border-radius: 50%;
    border: 7px solid var(--ring-white);
    box-shadow: 0 2px 6px rgba(0,0,0,0.25);
  }
  .hero-photo--staff {
    left: 431px;
    background: radial-gradient(circle at 50% 40%, #f3f3f3 0%, #d9dde2 45%, #6aa6b8 100%);
  }
  .hero-photo--certificate {
    left: 687px;
    background: radial-gradient(circle at 50% 50%, #f6f4ee 0%, #e8e4d8 50%, #2b2b2b 100%);
  }
  .hero-photo--innovation {
    left: 949px;
    background: radial-gradient(circle at 55% 45%, #e6eef3 0%, #b9cfdc 55%, #7f9fb4 100%);
  }

  .service-column {
    position: absolute;
    top: 318px;
    width: 342px;
  }
  .service-column--training { left: 30px; }
  .service-column--certification { left: 438px; }
  .service-column--research { left: 829px; }

  .service-heading {
    font-family: "Oswald", "Arial Narrow", sans-serif;
    font-weight: 500;
    font-size: 40px;
    line-height: 48px;
    color: var(--heading-red);
    text-transform: uppercase;
    margin-bottom: 4px;
  }
  .service-text {
    font-size: 13.7px;
    line-height: 18.6px;
    color: var(--body-text);
    text-align: justify;
    hyphens: auto;
    margin-bottom: 18.6px;
  }

  .brand-mark {
    position: absolute;
    left: 836px; top: 838px;
    display: flex;
    align-items: center;
    gap: 12px;
    color: var(--logo-navy);
    font-family: "Open Sans", Arial, sans-serif;
    font-weight: 700;
  }
  .brand-mark__dot {
    width: 64px; height: 64px;
    border-radius: 50%;
    background: var(--heading-red);
  }
  .brand-mark__name {
    font-size: 54px;
    line-height: 1;
    letter-spacing: 1px;
  }
  .brand-mark__full {
    font-size: 12px;
    line-height: 14px;
    width: 110px;
  }
</style>
</head>
<body>
  <main class="brochure-page">
    <header>
      <div class="hero-band"></div>
      <div class="hero-rule"></div>
      <h1 class="hero-title">Lorem ipsum dolor sit amet, consectetur adipiscing elit</h1>
      <div class="hero-photo hero-photo--staff" role="img" aria-label="Photo of three healthcare professionals in scrubs and a white coat"></div>
      <div class="hero-photo hero-photo--certificate" role="img" aria-label="Photo of a framed fellowship certificate"></div>
      <div class="hero-photo hero-photo--innovation" role="img" aria-label="Photo of a hand touching floating digital healthcare icons"></div>
    </header>

    <section class="service-column service-column--training">
      <h2 class="service-heading">Training</h2>
      <p class="service-text">Lorem ipsum dolor sit amet, consectetur adipiscing elit. Donec id lectus id ipsum sagittis mattis in eu nulla. Aenean sit amet malesuada risus. Curabitur dapibus ante magna, nec rhoncus sapien sodales in. Quisque consequat tincidunt leo, nec condimentum nunc fermentum sed. Cras sodales interdum tempus. Suspendisse massa ante, euismod sit amet bibendum in, gravida eu nulla. Curabitur sodales orci est, sit amet molestie mauris tincidunt quis. Nulla at nulla ut felis cursus porttitor vitae eget dolor. Aenean lobortis velit a magna ornare luctus eget eget tellus. Mauris a ipsum risus. Nam diam augue, adipiscing eu auctor et, adipiscing a nibh. Mauris vitae sagittis turpis. Vestibulum ante ipsum primis in faucibus orci luctus et ultrices posuere cubilia Curae; Nullam fringilla tellus justo, at commodo risus imperdiet et.</p>
      <p class="service-text">Sed et scelerisque nibh. Nulla bibendum mauris molestie velit consectetur, in pharetra tortor pellentesque. Morbi mi ante, condimentum a euismod quis, scelerisque ut sapien. Morbi ac pretium erat. Sed posuere varius ante imperdiet faucibus. Nulla sed dui quis eros varius egestas quis tempus diam. Integer gravida mauris non tempor adipiscing.</p>
      <p class="service-text">Morbi vestibulum tortor in massa tempus feugiat ac sit amet lorem. Fusce adipiscing ligula id massa tincidunt aliquet.</p>
    </section>

    <section class="service-column service-column--certification">
      <h2 class="service-heading">NCCS Certification</h2>
      <p class="service-text">Lorem ipsum dolor sit amet, consectetur adipiscing elit. Donec id lectus id ipsum sagittis mattis in eu nulla. Aenean sit amet malesuada risus. Curabitur dapibus ante magna, nec rhoncus sapien sodales in. Quisque consequat tincidunt leo, nec condimentum nunc fermentum sed. Cras sodales interdum tempus. Suspendisse massa ante, euismod sit amet bibendum in, gravida eu nulla. Curabitur sodales orci est, sit amet molestie mauris tincidunt quis. Nulla at nulla ut felis cursus porttitor vitae eget dolor. Aenean lobortis velit a magna ornare luctus eget eget tellus. Mauris a ipsum risus. Nam diam augue, adipiscing eu auctor et, adipiscing a nibh. Mauris vitae sagittis turpis. Vestibulum ante ipsum primis in faucibus orci luctus et ultrices posuere cubilia Curae; Nullam fringilla tellus justo, at commodo risus imperdiet et.</p>
      <p class="service-text">Sed et scelerisque nibh. Nulla bibendum mauris molestie velit consectetur, in pharetra tortor pellentesque. Morbi mi ante, condimentum a euismod quis, scelerisque ut sapien. Morbi ac pretium erat. Sed posuere varius ante imperdiet faucibus. Nulla sed dui quis eros varius egestas quis tempus diam. Integer gravida mauris non tempor adipiscing.</p>
    </section>

    <section class="service-column service-column--research">
      <h2 class="service-heading">Research</h2>
      <p class="service-text">Lorem ipsum dolor sit amet, consectetur adipiscing elit. Donec id lectus id ipsum sagittis mattis in eu nulla. Aenean sit amet malesuada risus. Curabitur dapibus ante magna, nec rhoncus sapien sodales in. Quisque consequat tincidunt leo, nec condimentum nunc fermentum sed. Cras sodales interdum tempus. Suspendisse massa ante, euismod sit amet bibendum in, gravida eu nulla. Curabitur sodales orci est, sit amet molestie mauris tincidunt quis. Nulla at nulla ut felis cursus porttitor vitae eget dolor. Aenean lobortis velit a magna ornare luctus eget eget tellus. Mauris a ipsum risus. Nam diam augue, adipiscing eu auctor et, adipiscing a nibh. Mauris vitae sagittis turpis. Vestibulum ante ipsum primis in faucibus orci luctus et ultrices posuere cubilia Curae; Nullam fringilla tellus justo, at commodo risus imperdiet et.</p>
      <p class="service-text">Sed et scelerisque nibh. Nulla bibendum mauris molestie velit consectetur, in pharetra tortor pellentesque. Morbi mi ante, condimentum a euismod quis, scelerisque ut sapien. Morbi ac pretium erat. Sed posuere varius ante imperdiet faucibus. Nulla sed dui quis eros varius egestas quis tempus diam. Integer gravida mauris non tempor adipiscing.</p>
    </section>

    <footer class="brand-mark">
      <span class="brand-mark__dot" aria-hidden="true"></span>
      <span class="brand-mark__name">NCCS</span>
      <span class="brand-mark__full">Northbrook Council of Clinical Standards</span>
    </footer>
  </main>
</body>
</html>
```